Cobblestone Schools Vinyl Banner

Based on the attached images design a image that we will be printed onto a vinyl Banner and used at conventions.

Design liberties are welcome but it needs to look good and the the final submission will need to be submitted in .psd format with all layers being able to be edited.

Make it look good and atract new business

```html
<!DOCTYPE html>
<html lang="en">
<head>
<meta charset="utf-8">
<title>Cobblestone Schools Vinyl Banner</title>
<link href="https://fonts.googleapis.com/css2?family=Bebas+Neue&family=Montserrat:wght@500;700&family=Roboto:wght@700&display=swap" rel="stylesheet">
<style>
  :root {
    --page: #ffffff;
    --panel: #f6f6f6;
    --brand-blue: #2f6aa3;
    --ink: #2b2b2b;
    --board-dark: #2e3133;
    --board-mid: #5a5f62;
    --logo-box: #ececec;
    --logo-ink: #3d4a6b;
    --white: #ffffff;
  }
  html, body {
    margin: 0;
    padding: 0;
    width: 1200px;
    height: 846px;
    overflow: hidden;
    background: var(--page);
  }
  .banner {
    position: absolute;
    left: 50px;
    top: 242px;
    width: 1100px;
    height: 360px;
    background: var(--panel);
    box-shadow: 0 14px 26px rgba(0,0,0,0.18);
    overflow: hidden;
  }
  .banner-art {
    position: absolute;
    inset: 0;
  }
  .how-title {
    position: absolute;
    left: 656px;
    top: 44px;
    margin: 0;
    font-family: "Montserrat", sans-serif;
    font-weight: 700;
    font-size: 29px;
    letter-spacing: 0.3px;
    color: var(--white);
    padding-bottom: 3px;
    border-bottom: 3px solid var(--white);
    line-height: 1.1;
  }
  .headline {
    position: absolute;
    left: 51px;
    top: 196px;
    margin: 0;
    font-family: "Bebas Neue", sans-serif;
    font-weight: 400;
    font-size: 58px;
    line-height: 1;
    color: var(--ink);
    white-space: nowrap;
  }
  .phone-pill {
    position: absolute;
    left: 123px;
    top: 260px;
    width: 337px;
    height: 42px;
    border-radius: 14px;
    background: var(--brand-blue);
    display: flex;
    align-items: center;
    justify-content: center;
    gap: 14px;
    color: var(--white);
    font-family: "Roboto", sans-serif;
    font-weight: 700;
    font-size: 35px;
    letter-spacing: 1px;
  }
  .phone-icon {
    width: 32px;
    height: 32px;
  }
  .website {
    position: absolute;
    left: 123px;
    width: 337px;
    top: 312px;
    text-align: center;
    font-family: "Roboto", sans-serif;
    font-weight: 700;
    font-size: 21px;
    color: var(--brand-blue);
  }
  .brand-box {
    position: absolute;
    left: 724px;
    top: 259px;
    width: 212px;
    height: 79px;
    border-radius: 6px;
    background: var(--logo-box);
  }
  .brand-name {
    position: absolute;
    left: 14px;
    top: 14px;
    display: flex;
    align-items: center;
    gap: 8px;
    font-family: "Montserrat", sans-serif;
    font-weight: 700;
    font-size: 17px;
    line-height: 1.05;
    color: var(--logo-ink);
    text-transform: uppercase;
  }
  .brand-square {
    width: 30px;
    height: 30px;
    background: var(--logo-ink);
    flex: none;
  }
  .brand-tagline {
    position: absolute;
    left: 0;
    right: 0;
    bottom: 6px;
    text-align: center;
    font-family: "Montserrat", sans-serif;
    font-weight: 500;
    font-size: 8.5px;
    color: var(--logo-ink);
  }
</style>
</head>
<body>
  <div class="banner">
    <svg class="banner-art" width="1100" height="360" viewBox="0 0 1100 360" aria-hidden="false">
      <defs>
        <linearGradient id="boardTone" x1="0" y1="0" x2="1" y2="1">
          <stop offset="0" stop-color="#3a3e40"/>
          <stop offset="0.5" stop-color="#555a5d"/>
          <stop offset="1" stop-color="#2e3133"/>
        </linearGradient>
        <linearGradient id="familyTone" x1="0" y1="0" x2="1" y2="0">
          <stop offset="0" stop-color="#d9c3b0"/>
          <stop offset="0.3" stop-color="#b98e6e"/>
          <stop offset="0.55" stop-color="#9fb9d8"/>
          <stop offset="0.8" stop-color="#3d4f56"/>
          <stop offset="1" stop-color="#8a6a55"/>
        </linearGradient>
      </defs>
      <rect class="photo-classroom" role="img" aria-label="Photo: six smiling children in front of a chalkboard raising chalk in the air" x="480" y="0" width="620" height="260" fill="url(#boardTone)"/>
      <path class="photo-family" role="img" aria-label="Photo: parents beside a smiling boy using a tablet" d="M0 0 H506 L578 215 H0 Z" fill="url(#familyTone)"/>
      <path class="lower-panel" d="M0 196 C 90 162, 180 147, 260 148 C 420 151, 560 236, 750 238 C 900 240, 1020 212, 1100 188 L1100 360 L0 360 Z" fill="var(--panel)"/>
      <path class="wave-line" d="M0 196 C 90 162, 180 147, 260 148 C 420 151, 560 236, 750 238 C 900 240, 1020 212, 1100 188" fill="none" stroke="var(--brand-blue)" stroke-width="4"/>
    </svg>

    <h2 class="how-title">HOW DOES IT WORK?</h2>

    <h1 class="headline">Sign up for free trial today!</h1>

    <div class="phone-pill">
      <svg class="phone-icon" viewBox="0 0 32 32" aria-hidden="true">
        <rect x="2" y="2" width="28" height="28" rx="7" fill="none" stroke="#fff" stroke-width="2.6"/>
        <path d="M11 8.5c1-.6 2-.3 2.5.6l1.3 2.4c.4.8.2 1.6-.5 2.1l-1 .7c.9 2 2.4 3.6 4.4 4.6l.8-1c.5-.7 1.4-.8 2.1-.4l2.4 1.4c.9.5 1.1 1.6.5 2.4l-1 1.3c-.8 1-2.2 1.3-3.4.8-4.4-1.9-7.6-5.2-9.4-9.6-.5-1.2-.1-2.6.9-3.3z" fill="#fff"/>
      </svg>
      <span>03 9555 0142</span>
    </div>

    <div class="website">www.cobblestoneschools.com.au</div>

    <div class="brand-box">
      <div class="brand-name">
        <span class="brand-square"></span>
        <span>Cobblestone<br>Schools</span>
      </div>
      <div class="brand-tagline">The Complete Online School Payment Solution</div>
    </div>
  </div>
</body>
</html>
```